Editorial Website Design for High-End Custom Millwork Firm

Design (no development) for a 5-7 page website for a high-end custom architectural millwork firm. Editorial, magazine-quality aesthetic — think Dwelling Quarterly and top-tier millwork studios (Owen Tallard, Vorko). Full brief, reference sites, and project photography attached. We have uploaded a sample of our photography to use in your design. PLEASE READ PDF DOCUMENT BRIEF!!!

```html
<!DOCTYPE html>
<html lang="en">
<head>
<meta charset="utf-8">
<title>Harlow Millwork — Project Portfolio</title>
<link rel="stylesheet" href="https://fonts.googleapis.com/css2?family=Newsreader:ital,opsz,wght@0,6..72,400;1,6..72,400&family=Inter:wght@400;500;600&display=swap">
<style>
  :root{
    --ink:#1c1b1a;
    --charcoal:#252424;
    --paper:#f9f8f6;
    --muted:#5c5a57;
    --rule:#e7e4df;
    --bronze:#5b4c40;
    --footer-text:#a9a6a1;
    --footer-head:#e9e6e1;
  }
  *{margin:0;padding:0;box-sizing:border-box}
  html,body{width:1200px;height:2344px;overflow:hidden}
  body{background:var(--paper);color:var(--ink);font-family:"Inter",sans-serif;position:relative}
  .serif{font-family:"Newsreader",serif}

  .site-header{position:absolute;left:0;top:0;width:1200px;height:74px;background:var(--charcoal);}
  .brand{position:absolute;left:66px;top:17px;font-family:"Newsreader",serif;font-size:30px;color:#fff;letter-spacing:-.3px}
  .main-nav{position:absolute;left:401px;top:30px;display:flex;gap:33px}
  .main-nav a{font-size:10.5px;font-weight:500;letter-spacing:1.1px;color:#fff;text-decoration:none;text-transform:uppercase}
  .main-nav a.active{color:#7d7770;border-bottom:2px solid #7d7770;padding-bottom:5px;margin-top:-3px}
  .inquire{position:absolute;left:1030px;top:20px;width:101px;height:33px;background:var(--bronze);color:#fff;font-size:10.5px;font-weight:600;letter-spacing:1.1px;display:flex;align-items:center;justify-content:center}

  .page-title{position:absolute;left:66px;top:94px;font-family:"Newsreader",serif;font-size:46px;font-weight:400;letter-spacing:-.3px}
  .intro{position:absolute;left:66px;top:161px;width:500px;font-size:15px;line-height:25px;color:var(--muted)}
  .filters{position:absolute;right:68px;top:191px;display:flex;gap:27px}
  .filters span{font-size:10.5px;letter-spacing:.8px;color:var(--muted)}
  .filters span.active{color:var(--ink);font-weight:600;border-bottom:2px solid var(--ink);padding-bottom:5px}
  .rule{position:absolute;left:66px;width:1066px;height:1px;background:var(--rule)}

  .project{position:absolute;width:328px}
  .project .photo{height:355px}
  .project h2{font-family:"Newsreader",serif;font-weight:400;font-size:30px;line-height:34px;margin-top:19px;letter-spacing:-.2px}
  .project .meta{font-size:10px;font-weight:500;letter-spacing:.8px;color:var(--muted);margin-top:4px;text-transform:uppercase}

  .eyebrow{position:absolute;left:0;width:1200px;top:1432px;text-align:center;font-size:11px;letter-spacing:3.5px;color:var(--muted)}
  .quote{position:absolute;left:0;width:1200px;top:1470px;text-align:center;font-family:"Newsreader",serif;font-style:italic;font-size:76px;line-height:77px;letter-spacing:-1.5px}
  .cta{position:absolute;left:498px;top:1738px;width:202px;padding-bottom:8px;border-bottom:2px solid var(--ink);display:flex;justify-content:space-between;align-items:center;font-size:10.5px;font-weight:600;letter-spacing:1px}

  .site-footer{position:absolute;left:0;top:1848px;width:1200px;height:496px;background:var(--charcoal);color:var(--footer-text);font-size:13.5px;line-height:21.5px}
  .footer-col{position:absolute;top:0}
  .footer-brand{font-family:"Newsreader",serif;font-size:30px;color:#fff;margin-top:96px;margin-bottom:24px}
  .footer-head{color:var(--footer-head);font-size:13px;letter-spacing:1.4px;margin-top:102px;margin-bottom:24px}
  .footer-col a{color:var(--footer-text)}
  .links li{list-style:none;margin-bottom:12.5px}
  .links li.spaced{letter-spacing:1px;margin-bottom:6px}
  .mbe{font-weight:600;color:#c4c1bb;margin-bottom:21px}
</style>
</head>
<body>
<header class="site-header">
  <div class="brand">Harlow Millwork</div>
  <nav class="main-nav">
    <a class="active">Projects</a><a>Capabilities</a><a>Sustainability</a><a>About</a><a>Contact</a>
  </nav>
  <div class="inquire">INQUIRE</div>
</header>

<h1 class="page-title">Project Portfolio</h1>
<p class="intro">A curated selection of our architectural millwork, spanning bespoke residential interiors and high-traffic commercial environments.</p>
<div class="filters"><span class="active">All Work</span><span>Commercial</span><span>Residential</span></div>
<div class="rule" style="top:245px"></div>

<article class="project" style="left:66px;top:298px">
  <div class="photo" role="img" aria-label="Executive reception desk with walnut panels and laser-cut screen" style="background:linear-gradient(180deg,#c9c6c2 0%,#5b4030 45%,#7a6a5e 100%)"></div>
  <h2>Skyline Reception</h2><div class="meta">Commercial — Executive Suite</div>
</article>
<article class="project" style="left:435px;top:298px">
  <div class="photo" role="img" aria-label="Light oak kitchen with marble backsplash" style="background:linear-gradient(180deg,#1c1b1a 0 3px,#e6e2dc 3px,#d6c6aa 60%,#bfb3a3 calc(100% - 3px),#1c1b1a calc(100% - 3px))"></div>
  <h2>Oak Haven Kitchen</h2><div class="meta">Residential — Bespoke Culinary</div>
</article>
<article class="project" style="left:803px;top:298px">
  <div class="photo" role="img" aria-label="Knotty pine library study with built-in bookshelves" style="background:linear-gradient(180deg,#f1ece4 0%,#d5b88e 40%,#b88752 100%)"></div>
  <h2>Heritage Library</h2><div class="meta">Residential — Custom Study</div>
</article>

<article class="project" style="left:66px;top:803px">
  <div class="photo" role="img" aria-label="Open-plan kitchen with walnut cabinetry and dark stone island" style="background:linear-gradient(180deg,#ece8e2 0%,#a6784b 50%,#4a4542 100%)"></div>
  <h2>Modernist Atelier</h2><div class="meta">Residential — Open Concept</div>
</article>
<article class="project" style="left:435px;top:803px">
  <div class="photo" role="img" aria-label="Hospitality lounge with wood slat ceiling and velvet sofa" style="width:284px;background:linear-gradient(180deg,#8d6e52 0%,#5d4a3e 50%,#3d4867 100%)"></div>
  <h2>Luxe Corporate<br>Lounge</h2><div class="meta">Commercial — Hospitality</div>
</article>
<article class="project" style="left:803px;top:803px">
  <div class="photo" role="img" aria-label="Pale oak kitchen island with upholstered stools" style="background:linear-gradient(180deg,#eeebe6 0%,#d9ccba 45%,#9fa7a4 75%,#c2ad93 100%)"></div>
  <h2>Minimalist Island</h2><div class="meta">Residential — Premium Kitchen</div>
</article>

<div class="rule" style="top:1314px"></div>

<div class="eyebrow">EXCELLENCE IN WOOD</div>
<blockquote class="quote">"Precision in every<br>joint, character in<br>every grain."</blockquote>
<div class="cta"><span>DISCUSS YOUR NEXT PROJECT</span>
  <svg width="12" height="10" viewBox="0 0 12 10"><path d="M0 5h10M6 1l4 4-4 4" fill="none" stroke="#1c1b1a" stroke-width="1.4"/></svg>
</div>

<footer class="site-footer">
  <div class="footer-col" style="left:66px;width:255px">
    <div class="footer-brand">Harlow Millwork</div>
    <p>Working with the top designers and architects on the east coast to produce and install high end millwork in residential and commercial environments.<br>Harlow is a Minority Owned Business.<br>A Certified MBE.</p>
    <p style="margin-top:43px">All Rights Reserved. Harlow Architectural Millwork.</p>
  </div>
  <div class="footer-col" style="left:338px;width:250px">
    <div class="footer-head">LET'S TALK.</div>
    <p>Harlow Architectural Millwork<br>1150 Linden Row<br>Ashford, VA 22904<br>555.204.7731 phone<br>555.204.7740 fax<br><a>info@harlowmillwork.com</a></p>
  </div>
  <div class="footer-col" style="left:610px;width:250px">
    <div class="footer-head" style="margin-top:104px;margin-bottom:18px">QUICK LINKS</div>
    <ul class="links"><li>Projects</li><li>Individual Project</li><li>Services</li><li>Blogs</li><li>About Us</li><li class="spaced">Terms of Service</li><li class="spaced">Privacy Policy</li></ul>
  </div>
  <div class="footer-col" style="left:881px;width:310px">
    <div class="footer-head" style="margin-bottom:18px">GET IN TOUCH</div>
    <p class="mbe">Harlow Millwork is a Minority Owned Business<br>A Certified MBE</p>
    <p>Architects and Interior Designers please contact:<br>Daniel Ashcombe<br>Head of Commercial Design Services<br><a>daniel@harlowmillwork.com</a></p>
    <p style="margin-top:21px">General Contractor and Construction Managers please contact:<br>Peter Holloway<br>Head of Estimating<br><a>peter@harlowmillwork.com</a></p>
  </div>
</footer>
</body>
</html>
```